Belvanta - Awnings & Outdoor Blinds

We need a brochure design for out Australia based Awnings & Outdoor Blinds company.

We require 2 templates:

1. Product Specific. (For One Product) - Single or Double Sided A4
Must Include:
Our Logo, Product Description, Pictures,Product Features & Benefits (in point form) & Our Contact Details (Phone & Website).

2.Product Range (Our Full Range) - 8 Page A4 (2x A3 Folded In Half Printed Both Sides).
Must Include:
Page 1 - Front Cover - Title (Product Range) Cover With Our Logo & Photo/s.
Page 2 - About Us, Why Us & Warranty Information.
Page 3 - A Gallery (Just Photos Showcasing Our Work)
Page 4 - 3 Products Per Page (Image/s, Product Title & Brief Description).
Page 5 - 3 Products Per Page (Image/s, Product Title & Brief Description).
Page 6 - 3 Products Per Page (Image/s, Product Title & Brief Description).
Page 7 - 3 Products Per Page (Image/s, Product Title & Brief Description).
Page 8 - Back Cover with our Contact Details (Phone, Website & Logo).

We are just looking for templates we will fill in all the content, needs to be easy to customise (change photos/text etc).

For more info on what we do: http://site7305.example-builder.com/belvanta

Requirements
Nice to have
• Nice to have the product pages 4 - 7 not as identical layout.

Nice to be in our colours Red, White, Black, Light Grey. (See Logo Variations - Logo is the top one).

```html
<!DOCTYPE html>
<html lang="en">
<head>
<meta charset="utf-8">
<title>Belvanta Direct – Folding Arm Awnings Brochure</title>
<link rel="stylesheet" href="https://fonts.googleapis.com/css2?family=Open+Sans:wght@300;400;600&display=swap">
<style>
  :root {
    --red: #c1272f;
    --red-deep: #a81f2a;
    --grey-band: #d4d4d6;
    --grey-block: #cfcfd1;
    --grey-text: #8e8e90;
    --ink: #3a3a3c;
    --white: #ffffff;
    --page-edge: #e2e2e2;
  }
  * { margin: 0; padding: 0; box-sizing: border-box; }
  html, body { width: 1200px; height: 850px; overflow: hidden; background: var(--white); }
  body { position: relative; font-family: "Open Sans", Arial, sans-serif; color: var(--ink); }

  .page { position: absolute; top: 24px; width: 566px; height: 806px; background: var(--white); border: 1px solid var(--page-edge); overflow: hidden; }
  .page--front { left: 22px; }
  .page--back { left: 611px; }

  .block { position: absolute; }
  .photo { position: absolute; }

  /* photo tones */
  .tone-wall   { background: linear-gradient(160deg, #d9d3c6 0%, #a9a296 55%, #6f6a62 100%); }
  .tone-facade { background: linear-gradient(180deg, #7fb1dd 0%, #b7c7cf 30%, #a79d8c 60%, #6c6458 100%); }
  .tone-pool   { background: linear-gradient(180deg, #86bde6 0%, #d8d2c4 50%, #4fa9c9 100%); }
  .tone-shade  { background: linear-gradient(180deg, #4c5352 0%, #8b948f 50%, #cfd4cd 100%); }
  .tone-white  { background: linear-gradient(170deg, #e9ebec 0%, #bcc4c6 50%, #6ab8cf 100%); }
  .tone-patio  { background: linear-gradient(180deg, #cfe4f2 0%, #e4e4e2 45%, #b0aeab 80%, #8bb9c9 100%); }
  .tone-house  { background: linear-gradient(180deg, #9cc3e1 0%, #c9c3b5 40%, #8f8a80 75%, #84a86a 100%); }
  .tone-deck   { background: linear-gradient(180deg, #8cc1e6 0%, #c6b79a 35%, #f2efe8 55%, #6e5a44 80%, #3aa5cf 100%); }
  .tone-terrace{ background: linear-gradient(180deg, #9ec8e4 0%, #5d6360 35%, #b9bdb6 70%, #dcdcd8 100%); }

  /* front page */
  .title-bar { left: 161px; top: 0; width: 405px; height: 77px; background: var(--red); display: flex; align-items: center; justify-content: center; }
  .title-bar h1 { color: var(--white); font-weight: 600; font-size: 21px; letter-spacing: 0.5px; }
  .grey-band { left: 0; top: 300px; width: 566px; height: 343px; background: var(--grey-band); }
  .thumb-panel { left: 147px; top: 241px; width: 419px; height: 141px; background: var(--red); }
  .intro { position: absolute; left: 35px; top: 407px; width: 500px; font-size: 12.4px; font-weight: 300; line-height: 1.3; color: var(--grey-text); text-transform: uppercase; text-align: justify; }
  .features { position: absolute; left: 290px; top: 492px; width: 258px; }
  .section-title { font-size: 14px; font-weight: 600; color: var(--red); margin-bottom: 2px; }
  .bullets { list-style: none; font-size: 9.6px; font-weight: 300; line-height: 1.38; color: #5a5a5c; }
  .bullets li { position: relative; padding-left: 9px; text-align: justify; }
  .bullets li::before { content: "•"; position: absolute; left: 0; }
  .bullets li + li { margin-top: 12px; }
  .site { position: absolute; left: 35px; top: 752px; font-size: 10.5px; color: var(--grey-text); letter-spacing: 0.8px; }

  .brand { position: absolute; display: flex; flex-direction: column; }
  .brand__row { display: flex; align-items: center; gap: 8px; }
  .brand__dot { width: 34px; height: 34px; border-radius: 50%; background: var(--red); flex-shrink: 0; }
  .brand__name { font-size: 30px; font-weight: 400; color: #222224; letter-spacing: -0.5px; line-height: 1; }
  .brand__tag { font-size: 7px; letter-spacing: 3.2px; color: #555; margin-left: 46px; margin-top: 4px; }
  .brand--front { left: 232px; top: 708px; }
  .brand--back { left: 312px; top: 728px; }
  .brand--back .brand__dot { width: 30px; height: 30px; }
  .brand--back .brand__name { font-size: 26px; }
  .brand--back .brand__tag { font-size: 6.2px; margin-left: 40px; }

  /* back page */
  .grey-column { left: 0; top: 0; width: 191px; height: 488px; background: var(--grey-block); }
  .grey-tile { left: 318px; top: 202px; width: 118px; height: 125px; background: var(--grey-block); }
  .red-side { left: 441px; top: 334px; width: 125px; height: 154px; background: var(--red); }
  .red-band { left: 196px; top: 488px; width: 370px; height: 169px; background: var(--red); }
  .red-band-left { left: 0; top: 488px; width: 196px; height: 169px; background: var(--red-deep); }
  .specs { position: absolute; left: 200px; top: 513px; width: 340px; color: var(--white); }
  .specs h2 { font-size: 13.6px; font-weight: 600; margin-bottom: 1px; }
  .specs .bullets { color: var(--white); font-size: 9.8px; }
  .specs .bullets li + li { margin-top: 0; }
  .specs section + section { margin-top: 9px; }
  .contact { position: absolute; left: 38px; top: 683px; font-size: 10.2px; font-weight: 300; line-height: 1.45; color: var(--grey-text); font-style: normal; }
  .contact .hours { margin-top: 11px; }
</style>
</head>
<body>

<article class="page page--front">
  <div class="photo tone-wall" style="left:0;top:0;width:153px;height:77px" role="img" aria-label="Close view of a folding arm awning against a stone wall"></div>
  <header class="block title-bar"><h1>FOLDING ARM AWNINGS</h1></header>
  <div class="block grey-band"></div>
  <div class="photo tone-facade" style="left:0;top:85px;width:566px;height:253px" role="img" aria-label="Modern stone home with red folding arm awnings over a patio"></div>
  <div class="block thumb-panel"></div>
  <div class="photo tone-pool" style="left:161px;top:249px;width:120px;height:128px" role="img" aria-label="Awning shading a poolside pavilion"></div>
  <div class="photo tone-shade" style="left:289px;top:249px;width:120px;height:128px" role="img" aria-label="Dark awning extended over a terrace with loungers"></div>
  <div class="photo tone-white" style="left:416px;top:249px;width:120px;height:128px" role="img" aria-label="White awning above a pool deck"></div>

  <p class="intro">Our folding arm awnings incorporate innovative new designs, reflecting today's demands for function, design and construction. These awnings are discreet, timeless designs that fit seamlessly in every setting, and can be neatly rolled away when not in use.</p>

  <div class="photo tone-patio" style="left:0;top:488px;width:273px;height:155px" role="img" aria-label="Awning over a bright patio with yellow chairs beside a pool"></div>
  <section class="features">
    <h2 class="section-title">Features &amp; Benefits</h2>
    <ul class="bullets">
      <li>Durable fabrics: Many of the fabrics we use are manufactured in Australia to suit local conditions. Choose from sunscreen, acrylic or canvas fabrics knowing they will look great for many years.</li>
      <li>Technically superior materials: We make our Drop-Arm Fabric Awnings from components that have been engineered to last in Australia's harsh conditions.</li>
    </ul>
  </section>

  <p class="site">WWW.BELVANTADIRECT.COM</p>
  <div class="brand brand--front">
    <div class="brand__row"><span class="brand__dot"></span><span class="brand__name">Belvanta Direct</span></div>
    <span class="brand__tag">Awnings &amp; Outdoor Blinds</span>
  </div>
</article>

<article class="page page--back">
  <div class="block grey-column"></div>
  <div class="photo tone-deck" style="left:69px;top:125px;width:120px;height:361px" role="img" aria-label="Tall view of an awning over a deck and pool"></div>
  <div class="photo tone-house" style="left:196px;top:0;width:370px;height:194px" role="img" aria-label="Contemporary home with grey folding arm awnings over an outdoor dining area"></div>
  <div class="photo tone-shade" style="left:196px;top:202px;width:118px;height:125px" role="img" aria-label="Dark awning above a pool with mountain view"></div>
  <div class="block grey-tile"></div>
  <div class="photo tone-white" style="left:441px;top:202px;width:125px;height:125px" role="img" aria-label="White awning edge against a wall"></div>
  <div class="photo tone-terrace" style="left:196px;top:334px;width:245px;height:153px" role="img" aria-label="Grey awning over a sliding door terrace with sea view"></div>
  <div class="block red-side"></div>
  <div class="block red-band-left"></div>
  <div class="block red-band"></div>

  <div class="specs">
    <section>
      <h2>Operation</h2>
      <ul class="bullets"><li>Crank Operated (Gearbox) as standard, Can also be motorised with optional Sun &amp; Wind sensor options.</li></ul>
    </section>
    <section>
      <h2>Available Fabrics</h2>
      <ul class="bullets"><li>Available in our Sunscreen &amp; Block Out fabrics.</li></ul>
    </section>
    <section>
      <h2>Specifications</h2>
      <ul class="bullets"><li>Maximum Width: 8000mm, Maximum Projection: 3500mm.</li></ul>
    </section>
  </div>

  <address class="contact">
    Unit 8 - 42 Harlow St,<br>
    Westbrook Brisbane QLD 4350<br>
    Phone: 1300 482 716<br>
    Email: info@belvanta.com.au<br>
    WWW.BELVANTADIRECT.COM
    <div class="hours">Trading Hours: Mon to Fri : 8am - 4pm</div>
  </address>

  <div class="brand brand--back">
    <div class="brand__row"><span class="brand__dot"></span><span class="brand__name">Belvanta Direct</span></div>
    <span class="brand__tag">Awnings &amp; Outdoor Blinds</span>
  </div>
</article>

</body>
</html>
```